Brisk Ember - Stock Certificate

We need a custom designed stock certificate that represents the look of our company logo but also have a cool look compared to a standard stock certificate. We thinking we want the logo in gold. Our website is https://www.briskemberusa.example.

We are wanting the certificate to look very professional and really cool, we have sales agents that work for the company and we are creating a program by which the sales agents can gain ownership in the company. So the certificates need to have a very cool appeal and that provides a sense of pride in owning "Units" in Brisk Ember.

Reason: Extending so other board members can vote as well, thank you all!

Target Market(s)

Stock/Shareholders

Industry/Entity Type

It Company

Font styles to use
Script

Requirements
Must have
• Must look like a stock certificate, must use our logo which the psd file for it was attached.
Nice to have
• Nice to have the logo in gold

```html
<!DOCTYPE html>
<html lang="en">
<head>
<meta charset="utf-8">
<title>Brisk Ember – Stock Certificate</title>
<link rel="stylesheet" href="https://fonts.googleapis.com/css2?family=Open+Sans:wght@400&family=Arimo:wght@400;700&family=UnifrakturMaguntia&family=Pinyon+Script&display=swap">
<style>
  :root {
    --ink: #111111;
    --night: #050505;
    --gold: #e0a526;
    --paper-light: #f0f0f0;
    --paper-dark: #d6d6d6;
    --lace-light: #9a9a9a;
    --lace-dark: #4a4a4a;
    --ring: #f4f4f4;
  }
  html, body {
    margin: 0;
    padding: 0;
    width: 1200px;
    height: 900px;
    overflow: hidden;
    background: var(--night);
  }
  .certificate {
    display: block;
    width: 1200px;
    height: 900px;
  }
  .issuer-name, .certificate-number { font-family: "Open Sans", sans-serif; font-size: 14px; fill: var(--ink); }
  .issuer-note { font-family: "Open Sans", sans-serif; font-size: 9.5px; fill: var(--ink); }
  .title { font-family: "UnifrakturMaguntia", serif; font-size: 64px; fill: var(--ink); stroke: #ffffff; stroke-width: 1.2px; paint-order: stroke; }
  .script { font-family: "Pinyon Script", cursive; font-size: 17px; fill: var(--ink); }
  .holder { font-family: "Arimo", sans-serif; font-weight: 700; font-size: 28px; fill: var(--ink); }
  .shares { font-family: "Arimo", sans-serif; font-size: 19px; fill: var(--ink); }
  .rule { stroke: #333333; stroke-width: 0.8; }
  .seal-name { font-family: "Open Sans", sans-serif; font-size: 15px; fill: var(--gold); letter-spacing: 1px; }
</style>
</head>
<body>
<svg class="certificate" viewBox="0 0 820 615" preserveAspectRatio="none" xmlns="http://www.w3.org/2000/svg">
  <defs>
    <linearGradient id="paper" x1="0" y1="0" x2="0" y2="1">
      <stop offset="0" stop-color="var(--paper-light)"/>
      <stop offset="1" stop-color="var(--paper-dark)"/>
    </linearGradient>
    <radialGradient id="lace" cx="0.5" cy="0.5" r="0.6">
      <stop offset="0" stop-color="var(--lace-light)"/>
      <stop offset="1" stop-color="var(--lace-dark)"/>
    </radialGradient>
    <path id="title-arc" d="M125,292 Q410,172 700,294"/>
  </defs>

  <rect class="backdrop" width="820" height="615" fill="var(--night)"/>

  <path class="lace-border" role="img" aria-label="Ornamental guilloche lace border"
        d="M8,100 Q150,58 330,95 L490,95 Q670,58 812,100 L812,607 L8,607 Z" fill="url(#lace)"/>
  <circle class="seal-lace" role="img" aria-label="Ornamental lace ring around the seal"
          cx="410" cy="78" r="92" fill="url(#lace)"/>

  <path class="panel-gap" d="M42,143 A28,28 0 0 0 70,115 C200,112 280,120 325,168 A124,124 0 0 0 495,168 C540,120 620,112 750,115 A28,28 0 0 0 778,143 L778,532 A28,28 0 0 0 750,560 L70,560 A28,28 0 0 0 42,532 Z"
        fill="none" stroke="var(--night)" stroke-width="22"/>
  <path class="panel" d="M42,143 A28,28 0 0 0 70,115 C200,112 280,120 325,168 A124,124 0 0 0 495,168 C540,120 620,112 750,115 A28,28 0 0 0 778,143 L778,532 A28,28 0 0 0 750,560 L70,560 A28,28 0 0 0 42,532 Z"
        fill="url(#paper)" stroke="var(--gold)" stroke-width="3"/>

  <g class="seal">
    <circle cx="410" cy="78" r="62" fill="var(--night)" stroke="var(--ring)" stroke-width="2.5"/>
    <text class="seal-name" x="410" y="83" text-anchor="middle">Brisk Ember</text>
  </g>

  <g class="issuer" text-anchor="middle">
    <text class="issuer-name" x="186" y="159">Brisk Ember</text>
    <text class="issuer-note" x="186" y="174">Incorporated Under the Laws of the State of Texas</text>
  </g>
  <g class="registry" text-anchor="middle">
    <text class="certificate-number" x="633" y="159">Certificate No. 00137</text>
    <text class="issuer-note" x="633" y="174">Houston, Texas, United States of America</text>
  </g>

  <text class="title"><textPath href="#title-arc" startOffset="50%" text-anchor="middle">Stock Certificate</textPath></text>

  <g class="body" text-anchor="middle">
    <text class="script" x="410" y="286">This is to certify that</text>
    <text class="holder" x="410" y="322">MARLOW QUINN</text>
    <line class="rule" x1="185" y1="328" x2="633" y2="328"/>
    <text class="script" x="410" y="349">is the owner of</text>
    <text class="shares" x="410" y="377">One Hundred (100) Shares</text>
    <line class="rule" x1="260" y1="383" x2="560" y2="383"/>
    <text class="script" x="410" y="404">fully paid and non-assessable shares of Brisk Ember transferrable only on the books of the</text>
    <text class="script" x="410" y="424">Corporation by the holder thereof in person or by a duly authorized Attorney</text>
    <text class="script" x="410" y="445">upon surrender of this Certificate properly endorsed.</text>
    <text class="script" x="410" y="473">Witness, the seal of the Corporation and the signatures of its duly authorized officers</text>
    <text class="script" x="410" y="494">this _____ day of _____________, 2017.</text>
  </g>

  <g class="signatures" text-anchor="middle">
    <line class="rule" x1="105" y1="530" x2="330" y2="530"/>
    <text class="script" x="217" y="550">Secretary</text>
    <line class="rule" x1="490" y1="530" x2="713" y2="530"/>
    <text class="script" x="601" y="550">President</text>
  </g>
</svg>
</body>
</html>
```